New Bicycle shop business card

Hi!
I'm looking for a business card for my new proffesional bike mechanics shop. This shop is only for fixing broken bikes and not selling bikes.
Peferbly a modern and sleek and modern design.
Colors: black, grey, red, white
Information:
Name: Rijwielwerkplaats Vanhoutem
Shop owner: Bart Vanhoutem & Sanne Maertens
Website: www.rijwielwerkplaats-vanhoutem.be
Email: info@rijwielwerkplaats-vanhoutem.be
Phone number: +32471902386
Street adres: Kerkweg 64
9970 Oostmoere
Slogan/shop information: Herstellingen van alle merken.
Logo: see files.
Target Market(s)
People who seek a mechanic to fix or upgrade their bikes.
Contact Information for Business Card
Information:
Website: info@rijwielwerkplaats-vanhoutem.be
9970 Oostmoere
Logo: see files.

```html
<!DOCTYPE html>
<html lang="nl">
<head>
<meta charset="utf-8">
<title>Rijwielwerkplaats Vanhoutem – visitekaartje</title>
<link rel="stylesheet" href="https://fonts.googleapis.com/css2?family=Exo+2:wght@400;600;800&display=swap">
<style>
  :root {
    --bg: #3a3f46;
    --card: #0d0d0e;
    --card-edge: #1a1a1c;
    --red: #e3173e;
    --white: #ffffff;
    --grey: #b9b9bb;
    --silver: #8d8e92;
    --faint: #1b1b1d;
  }
  * { box-sizing: border-box; margin: 0; padding: 0; }
  html, body { width: 1200px; height: 900px; overflow: hidden; }
  body {
    background: var(--bg);
    font-family: "Exo 2", sans-serif;
    display: flex; flex-direction: column; align-items: center; justify-content: center;
    gap: 40px;
  }
  .card {
    position: relative;
    width: 660px; height: 377px;
    background: var(--card);
    overflow: hidden;
    box-shadow: 0 18px 40px rgba(0,0,0,.45);
  }

  /* Front */
  .owners {
    position: absolute; left: 40px; top: 30px;
    color: var(--white); font-weight: 800; font-size: 21px; letter-spacing: .3px;
    text-transform: uppercase;
  }
  .owners-rule {
    position: absolute; left: 250px; top: 62px; width: 180px; height: 1px;
    background: var(--red);
  }
  .role {
    position: absolute; left: 40px; top: 60px;
    background: var(--red); color: var(--white);
    font-weight: 600; font-size: 14px; padding: 2px 12px 3px;
    text-transform: uppercase;
  }
  .contact {
    position: absolute; left: 40px; top: 130px;
    list-style: none; color: var(--white); font-size: 13.5px; line-height: 22px;
  }
  .contact li { display: flex; align-items: center; gap: 9px; }
  .contact svg { width: 13px; height: 13px; flex: none; }
  .divider {
    position: absolute; left: 330px; top: 120px; width: 1px; height: 160px;
    background: #555;
  }
  .brand {
    position: absolute; left: 355px; top: 120px;
    display: flex; align-items: center; gap: 12px;
  }
  .brand-dot { width: 34px; height: 34px; border-radius: 50%; background: var(--red); flex: none; }
  .brand-name {
    color: var(--white); font-weight: 800; font-size: 22px; line-height: 1.05;
    text-transform: uppercase; letter-spacing: .5px;
  }
  .address {
    position: absolute; left: 370px; top: 214px;
    color: var(--white); font-size: 15px; line-height: 21px; letter-spacing: .6px;
    padding-top: 10px; border-top: 1px solid var(--red); width: 230px;
  }
  .slogan-band {
    position: absolute; left: 0; bottom: 32px; width: 560px; height: 40px;
    background: var(--red);
    display: flex; align-items: center; padding-left: 40px;
    color: var(--white); font-weight: 800; font-size: 17px; text-transform: uppercase;
  }
  .band-mark {
    position: absolute; left: 518px; bottom: 42px; width: 20px; height: 20px;
    background: var(--white);
  }
  .corner-tab {
    position: absolute; right: 40px; bottom: 32px; width: 40px; height: 40px;
    background: var(--grey);
  }

  /* Back */
  .back-circle {
    position: absolute; right: -60px; top: 40px; width: 320px; height: 320px;
    border-radius: 50%; background: var(--faint);
  }
  .back-name {
    position: absolute; left: 0; right: 0; top: 150px; text-align: center;
    color: var(--silver); font-weight: 800; font-size: 30px; line-height: 1.1;
    letter-spacing: 1px; text-transform: uppercase;
  }
</style>
</head>
<body>
  <section class="card card-front">
    <p class="owners">Bart Vanhoutem &amp; Sanne Maertens</p>
    <span class="owners-rule"></span>
    <p class="role">Shop owner</p>

    <ul class="contact">
      <li>
        <svg viewBox="0 0 16 16"><path fill="#e3173e" d="M3 1l3 3-2 2c1 2 3 4 5 5l2-2 3 3-2 3C7 15 1 9 0 4z"/></svg>
        +32471902386
      </li>
      <li>
        <svg viewBox="0 0 16 16"><circle cx="8" cy="8" r="7" fill="none" stroke="#e3173e" stroke-width="1.6"/><path d="M1 8h14M8 1c-3 4-3 10 0 14M8 1c3 4 3 10 0 14" fill="none" stroke="#e3173e" stroke-width="1.3"/></svg>
        www.rijwielwerkplaats-vanhoutem.be
      </li>
      <li>
        <svg viewBox="0 0 16 16"><rect x="1" y="3" width="14" height="10" fill="#e3173e"/><path d="M1 3l7 6 7-6" fill="none" stroke="#0d0d0e" stroke-width="1.3"/></svg>
        info@rijwielwerkplaats-vanhoutem.be
      </li>
    </ul>
    <span class="divider"></span>

    <div class="brand">
      <span class="brand-dot"></span>
      <p class="brand-name">Rijwielwerkplaats<br>Vanhoutem</p>
    </div>

    <p class="address">Kerkweg 64<br>9970 Oostmoere</p>

    <p class="slogan-band">Herstellingen van alle merken</p>
    <span class="band-mark"></span>
    <span class="corner-tab"></span>
  </section>

  <section class="card card-back">
    <span class="back-circle"></span>
    <p class="back-name">Rijwielwerkplaats<br>Vanhoutem</p>
  </section>
</body>
</html>
```